A5 Flyer for Financial Services Business

I am after a re-design of our business flyer to fit in with our new branding style and logo colour scheme. Wanting something with a bit of designer flair that I could not create myself. I have included the flyer which I created which lacks style so dazzle me.

I want to use the same content.

Text for main body of flyer is

Are you a small business owner, tradie or PAVC Service Provider struggling to stay on top of your bookkeeping and compliance obligations? If so we would love to help you get back on track and take control of your business finances so that you can make informed business decisions and focus on what you do best.

We have over 20 years industry experience and, as a small business ourselves, we are able to offer our clients a personal bookkeeping solution tailored to meet the needs of your business.

Accounts Payable | Accounts Receivable
Customer Invoicing
Bank and Credit Card Reconciliations
Payroll | Superannuation | Payroll Tax
Business Activity | Instalment Activity Statements
Regular Financial Reports
Ledgra and Tallybook Set-Up and Training

```html
<!DOCTYPE html>
<html lang="en">
<head>
<meta charset="utf-8">
<title>Even Ledger Financial Services – Bookkeeping Flyer</title>
<link href="https://fonts.googleapis.com/css2?family=Source+Sans+3:ital,wght@0,300;0,400;0,600;0,700;1,700&display=swap" rel="stylesheet">
<style>
  :root {
    --teal: #2a9a90;
    --teal-deep: #1f7d75;
    --teal-text: #25978c;
    --ink: #111111;
    --body: #222222;
    --white: #ffffff;
    --wood-light: #f3f3f1;
    --wood-mid: #dcdcda;
  }
  * { margin: 0; padding: 0; box-sizing: border-box; }
  html, body { width: 927px; height: 1200px; overflow: hidden; background: #ffffff; }
  .flyer {
    position: relative; width: 927px; height: 1200px; overflow: hidden;
    font-family: "Source Sans 3", "Myriad Pro", Arial, sans-serif;
  }
  .hero-photo {
    position: absolute; left: 0; top: 0; width: 927px; height: 598px;
    background: linear-gradient(160deg, var(--wood-light) 0%, #ebebe9 55%, var(--wood-mid) 100%);
  }
  .desk-photo {
    position: absolute; left: 455px; top: 0; width: 472px; height: 500px;
    background: radial-gradient(ellipse at 60% 40%, #f7f7f7 0%, #e2e4e4 45%, rgba(42,154,144,0.55) 80%, rgba(42,154,144,0) 100%);
  }
  .brand {
    position: absolute; left: 140px; top: 22px;
    display: flex; align-items: center; gap: 10px;
    color: var(--teal-deep); font-weight: 400;
  }
  .brand-mark { width: 26px; height: 26px; background: var(--teal-deep); }
  .brand-name { font-size: 19px; letter-spacing: 1.5px; line-height: 1.1; }
  .accent-bar { position: absolute; left: 0; top: 128px; width: 9px; height: 76px; background: var(--teal); }
  .headline {
    position: absolute; left: 64px; top: 126px; width: 480px;
    font-size: 67px; line-height: 63px; font-weight: 600; color: var(--ink); letter-spacing: -0.5px;
  }
  .lead {
    position: absolute; left: 64px; top: 340px; width: 520px;
    font-size: 26px; line-height: 36px; font-weight: 700; font-style: italic; color: var(--teal-text);
  }
  .intro {
    position: absolute; left: 64px; top: 478px; width: 560px;
    font-size: 20px; line-height: 25.5px; color: var(--body);
  }
  .services-band {
    position: absolute; left: 0; top: 598px; width: 927px; height: 602px; background: var(--teal);
  }
  .still-life-photo {
    position: absolute; left: 0; top: 598px; width: 410px; height: 602px;
    background: radial-gradient(ellipse at 40% 30%, #3a8f86 0%, #2f8b82 40%, var(--teal) 100%);
  }
  .about {
    position: absolute; right: 89px; top: 630px; width: 430px; text-align: right;
    font-size: 20.5px; line-height: 25.5px; font-weight: 600; color: var(--white);
  }
  .service-list {
    position: absolute; right: 67px; top: 787px; list-style: none; text-align: right;
    color: var(--white); font-size: 20px; line-height: 36.3px;
  }
  .service-list li { display: flex; justify-content: flex-end; align-items: center; gap: 8px; }
  .service-list svg { width: 18px; height: 18px; flex: none; }
  .rule { position: absolute; left: 227px; width: 614px; border-top: 2px dashed rgba(255,255,255,0.75); }
  .rule--top { top: 1052px; }
  .rule--bottom { top: 1116px; }
  .credentials {
    position: absolute; left: 229px; top: 1064px; display: flex; gap: 26px;
    color: var(--white); font-size: 23px; font-weight: 700;
  }
  .credentials span::before { content: "\25C6"; font-size: 17px; margin-right: 6px; vertical-align: 2px; }
  .contact {
    position: absolute; left: 229px; top: 1118px; height: 50px; display: flex; align-items: center;
    color: var(--white);
  }
  .phone { font-size: 40px; font-weight: 300; letter-spacing: 0.5px; padding-right: 14px; border-right: 1px solid rgba(255,255,255,0.8); line-height: 46px; }
  .web { font-size: 21px; padding-left: 14px; }
</style>
</head>
<body>
<main class="flyer">
  <div class="hero-photo" role="img" aria-label="Photo of a white wooden desk top"></div>
  <div class="desk-photo" role="img" aria-label="Photo of a white calculator and clipboard with a teal swirling floral ornament"></div>

  <div class="brand">
    <span class="brand-mark"></span>
    <span class="brand-name">EVEN LEDGER<br>FINANCIAL SERVICES</span>
  </div>

  <div class="accent-bar"></div>
  <h1 class="headline">Bookkeeping tailored to your business needs</h1>
  <p class="lead">Are you a small business owner, tradie or PAVC Service Provider struggling to stay on top of your bookkeeping and compliance obligations?</p>
  <p class="intro">If so we would love to help you get back on track and take control of your business finances so that you can make informed business decisions and focus on what you do best.</p>

  <section class="services-band">
  </section>
  <div class="still-life-photo" role="img" aria-label="Photo of scattered coins and black reading glasses"></div>

  <p class="about">We have over 20 years industry experience and, as a small business ourselves, we are able to offer our clients a personal bookkeeping solution tailored to meet the needs of your business.</p>

  <ul class="service-list">
    <li>Accounts Payable | Accounts Receivable <svg viewBox="0 0 18 18"><rect x="1" y="3" width="13" height="13" fill="none" stroke="#fff" stroke-width="1.5"/><path d="M4 9l3.5 3.5L17 2" fill="none" stroke="#fff" stroke-width="2"/></svg></li>
    <li>Customer Invoicing <svg viewBox="0 0 18 18"><rect x="1" y="3" width="13" height="13" fill="none" stroke="#fff" stroke-width="1.5"/><path d="M4 9l3.5 3.5L17 2" fill="none" stroke="#fff" stroke-width="2"/></svg></li>
    <li>Bank and Credit Card Reconciliations <svg viewBox="0 0 18 18"><rect x="1" y="3" width="13" height="13" fill="none" stroke="#fff" stroke-width="1.5"/><path d="M4 9l3.5 3.5L17 2" fill="none" stroke="#fff" stroke-width="2"/></svg></li>
    <li>Payroll | Superannuation | Payroll Tax <svg viewBox="0 0 18 18"><rect x="1" y="3" width="13" height="13" fill="none" stroke="#fff" stroke-width="1.5"/><path d="M4 9l3.5 3.5L17 2" fill="none" stroke="#fff" stroke-width="2"/></svg></li>
    <li>Business Activity | Instalment Activity Statements <svg viewBox="0 0 18 18"><rect x="1" y="3" width="13" height="13" fill="none" stroke="#fff" stroke-width="1.5"/><path d="M4 9l3.5 3.5L17 2" fill="none" stroke="#fff" stroke-width="2"/></svg></li>
    <li>Regular Financial Reports <svg viewBox="0 0 18 18"><rect x="1" y="3" width="13" height="13" fill="none" stroke="#fff" stroke-width="1.5"/><path d="M4 9l3.5 3.5L17 2" fill="none" stroke="#fff" stroke-width="2"/></svg></li>
    <li>Ledgra and Tallybook Set-Up and Training <svg viewBox="0 0 18 18"><rect x="1" y="3" width="13" height="13" fill="none" stroke="#fff" stroke-width="1.5"/><path d="M4 9l3.5 3.5L17 2" fill="none" stroke="#fff" stroke-width="2"/></svg></li>
  </ul>

  <div class="rule rule--top"></div>
  <div class="credentials">
    <span>Ledgra Certified Advisor</span>
    <span>Tallybook Pro Advisor</span>
  </div>
  <div class="rule rule--bottom"></div>

  <div class="contact">
    <span class="phone">0400 123 456</span>
    <span class="web">www.evenledgerfinancial.com.au</span>
  </div>
</main>
</body>
</html>
```